Home Page Concept For New Website (BookMyAdvisor)

We are creating a new website that allows students to schedule time to see their school counselors (bookmyadvisor.example). We need a concept for the home page. You will need to create one concept and provide a jpg image for us for review. The homepage needs to have at least a logon section, a Latest News section, a section for 3 Ads all 125x125 and some content for text where we describe the site. A menu will need to contain the following: Home, Pricing, Help and Contact Us.

You will need also need to create a design of the basic interior page template which should have a smaller banner, header, footer etc. This template will be used when we build the actual application and lots of space will be needed in the content area to draw controls such as textboxes, buttons, grids, etc in order to implement the application functionality when we code it.

We have no logo or color scheme so you are free to use your imagination as long as it looks professional.

Once we accept the design, you will need to give us a zip file containing all the artifacts including the .psd files, jpg images, and any fonts used, etc.
Updates

The customer has reviewed all the designs submitted so far and feels like most do not really convey that it is a scheduling site. They want all pictures removed because this will confuse students and students will think that the picture is their actual counselor. So remove the pictures of all the people and add illustrations, graphics, icons of some images that are related to scheduling like calendars, time, watches, etc. Fade images into the banners, or background etc. and be creative. Remember this site is for multiple schools to signup to use for scheduling their counselors so it needs to convey that function.

I sent this out before but I needed to repeat it for other designers... The customer has reviewed all the designs submitted so far and feels like most do not really convey that it is a scheduling site. They want all pictures removed because this will confuse students and students will think that the picture is their actual counselor. So remove the pictures of all the people and add illustrations, graphics, icons of some images that are related to scheduling like calendars, time, watches, etc. Fade images into the banners, or background etc. and be creative. Remember this site is for multiple schools to signup to use for scheduling their counselors so it needs to convey that function. Also several designers did not follow directions that clearly stated the home page had to include a login panel. The users of this system need to be able to login directly from this page. A login panel needs to contain the standard user name, password, login button, forgot my password link or button and maybe a signup link or button....nothing more. So please review your designs and update them accordingly. Thanks

Industry/Entity Type

School

Font styles to use
Sans Serif

Requirements
Should not have
• We don't have a logo or any pre-determined colors. We just need a clean professional design that fits pretty much on one page without a lot of scrolling. For example, the customer does NOT want a site like this..

https://hourlume.example/

where you scroll for days with large multi-color panels.

```html
<!DOCTYPE html>
<html lang="en">
<head>
<meta charset="utf-8">
<title>BookMyAdvisor — Home</title>
<link href="https://fonts.googleapis.com/css2?family=Oswald:wght@400;500&family=Open+Sans+Condensed:wght@300;700&family=Arvo:wght@700&family=Questrial&family=Arimo:wght@400;700&display=swap" rel="stylesheet">
<style>
  :root{
    --green:#6cbb10;
    --green-dark:#5aa20a;
    --ink:#222;
    --text:#666;
    --muted:#888;
    --panel:#e9e9e9;
    --footer:#e2e2e2;
    --charcoal:#4a4a4a;
    --white:#fff;
    --accent:#e06a10;
  }
  *{box-sizing:border-box;margin:0;padding:0}
  html,body{width:1065px;height:1200px;overflow:hidden;background:var(--white)}
  body{position:relative;font-family:"Open Sans Condensed","Arial Narrow",sans-serif;font-weight:300;color:var(--text)}
  .abs{position:absolute}

  /* header */
  .brand{left:43px;top:22px;display:flex;align-items:center;gap:10px}
  .brand-dot{width:53px;height:53px;border-radius:50%;background:var(--green)}
  .brand-name{font-family:"Oswald",sans-serif;font-weight:400;font-size:27px;color:var(--ink);letter-spacing:-.3px}
  .nav{right:36px;top:36px;display:flex;gap:6px;font-family:"Oswald",sans-serif;font-size:13.5px;letter-spacing:.2px}
  .nav a{color:#777;text-decoration:none;padding:5px 13px}
  .nav a.active{background:var(--green);color:var(--white)}

  /* hero */
  .hero{left:0;top:101px;width:1065px;height:504px;background:radial-gradient(ellipse at 60% 40%,#8a8a8a,#5e5e5e 70%,#505050)}
  .hero-title{left:0;width:1065px;top:280px;text-align:center;font-family:"Oswald",sans-serif;font-weight:500;font-size:46px;color:var(--white);letter-spacing:-.5px}
  .hero-copy{left:240px;width:585px;top:343px;text-align:center;font-size:17px;line-height:19px;color:var(--white)}
  .hero-btn{left:477px;top:410px;width:112px;height:39px;background:var(--white);color:var(--green);font-family:"Oswald",sans-serif;font-size:13.5px;display:flex;align-items:center;justify-content:center}
  .dots{left:490px;top:569px;display:flex;gap:9px}
  .dots i{width:9px;height:9px;background:#aaa;display:block}
  .dots i.on{background:var(--white)}

  /* content */
  .soft-band{left:0;top:830px;width:1065px;height:103px;background:linear-gradient(#fff,#f3f3f3)}
  .section-title{font-size:36px;color:var(--green);font-weight:300}
  .rule{height:6px;background:repeating-linear-gradient(90deg,#ccc 0 1px,transparent 1px 3px)}
  .welcome-title{left:41px;top:650px}
  .welcome-rule{left:41px;top:702px;width:605px}
  .lead{left:43px;top:728px;width:600px;font-size:15px;font-weight:700;color:#333;font-weight:300;color:#222}
  .para{left:43px;width:600px;font-size:13.8px;line-height:18.5px;color:var(--text)}
  .read-more{left:43px;top:894px;font-size:12.5px;color:var(--green)}

  .login-title{left:689px;top:650px}
  .login-rule{left:689px;top:702px;width:339px}
  .login-panel{left:688px;top:727px;width:339px;height:183px;background:var(--panel);border-radius:3px}
  .field-label{left:716px;font-size:13px;color:#333}
  .field{left:788px;width:209px;height:32px;background:var(--white);border:1px solid #ddd;border-radius:2px}
  .btn{height:30px;font-family:"Oswald",sans-serif;font-size:13.5px;color:var(--white);display:flex;align-items:center;justify-content:center}
  .btn-login{left:788px;top:845px;width:83px;background:var(--green)}
  .btn-new{left:884px;top:845px;width:91px;background:var(--charcoal)}
  .forgot{left:789px;top:884px;font-size:11.5px;color:var(--accent);text-decoration:underline}

  /* news */
  .news{left:42px;top:950px;width:611px;height:119px;border:1px solid #9ccf5c}
  .news-tag{left:42px;top:950px;width:115px;height:119px;background:var(--green);color:var(--white);font-size:33px;line-height:39px;padding:20px 0 0 26px}
  .news-arrow{left:157px;top:987px}
  .news-head{left:205px;top:963px;font-size:12.5px;color:#222}
  .news-date{left:207px;top:982px;font-size:11px;color:#999}
  .news-body{left:207px;top:998px;width:420px;font-size:11.5px;line-height:18.5px;color:#555}
  .news-pager{left:206px;top:1042px;font-size:14px;color:#444;letter-spacing:4px}

  /* ads */
  .ad{top:955px;width:105px;height:105px;display:flex;flex-direction:column;align-items:center;justify-content:center;text-align:center}
  .ad-one{left:689px;border:1px solid #222;background:var(--white)}
  .ad-one b{font-family:"Arvo",serif;font-size:12.5px;color:#e8a200}
  .ad-one span{font-family:"Arimo",sans-serif;font-size:12px;color:#222;margin-top:3px;letter-spacing:.5px}
  .ad-two{left:807px;background:repeating-linear-gradient(135deg,#3a3a3a 0 2px,#444 2px 4px);color:var(--white);font-family:"Questrial",sans-serif;font-size:15.5px;line-height:19px;letter-spacing:.5px}
  .ad-three{left:923px;background:#f4f4f4;border:1px solid #ddd;font-family:"Arimo",sans-serif}
  .ad-three b{font-size:15px;color:#555}
  .ad-three span{font-size:8.5px;color:#666;margin-top:6px}

  /* footer */
  .footer{left:0;top:1094px;width:1065px;height:106px;background:var(--footer)}
  .footer-shadow{left:100px;top:1094px;width:760px;height:12px;background:radial-gradient(ellipse at 50% 0,rgba(0,0,0,.18),transparent 70%)}
  .foot-links{left:43px;top:1122px;font-size:13.5px;color:#666}
  .foot-links .sep{margin:0 6px;color:#999}
  .copy{left:43px;top:1147px;font-size:13.5px;color:#777}
  .news-label{left:335px;top:1121px;font-size:13.5px;color:#666}
  .email{left:335px;top:1145px;width:151px;height:23px;background:var(--white);font-size:11px;color:#999;padding:4px 7px}
  .subscribe{left:486px;top:1145px;width:64px;height:23px;background:#333;color:var(--white);font-size:11.5px;display:flex;align-items:center;justify-content:center}
  .phone-icon{left:651px;top:1125px}
  .call-label{left:697px;top:1122px;font-size:13px;color:#666}
  .call-num{left:697px;top:1138px;font-size:20px;color:#888}
  .social{left:893px;top:1127px;display:flex;gap:5px}
  .social i{width:30px;height:30px;border-radius:50%;background:var(--white);display:block}
</style>
</head>
<body>

<header>
  <div class="abs brand"><span class="brand-dot"></span><span class="brand-name">BOOK MY ADVISOR</span></div>
  <nav class="abs nav">
    <a class="active" href="#">HOME</a><a href="#">PRICING</a><a href="#">HELP</a><a href="#">COUNSELLORS</a><a href="#">CONTACT US</a>
  </nav>
</header>

<section>
  <div class="abs hero" role="img" aria-label="Greyscale close-up of a clock face over a calendar page"></div>
  <h1 class="abs hero-title">DUIS AUTE IRURE DOLOR</h1>
  <p class="abs hero-copy">Consectetur adipisicing elit, sed do eiusmod tempor incididunt ut labore et dolore magna aliqua. Ut enim ad minim veniam, quis nostrud exercitation ullamco laboris nisi ut aliquip ex ea commodo consequat.</p>
  <a class="abs hero-btn">KNOW MORE</a>
  <div class="abs dots"><i class="on"></i><i></i><i></i><i></i><i></i></div>
</section>

<div class="abs soft-band"></div>

<section>
  <h2 class="abs section-title welcome-title">Welcome</h2>
  <div class="abs rule welcome-rule"></div>
  <p class="abs lead">Lorem ipsum dolor sit amet Consectetur adipisicing elit, sed do eiusmod tempor incididunt ut labore et dolore magna aliqua.</p>
  <p class="abs para" style="top:764px">Ut enim ad minim veniam, quis nostrud exercitation ullamco laboris nisi ut aliquip ex ea commodo consequat. Duis aute irure dolor in reprehenderit in voluptate velit esse cillum dolore eu fugiat nulla pariatur.<br>Excepteur sint occaecat cupidatat non proident, sunt in culpa qui officia deserunt mollit anim id est laborum.</p>
  <p class="abs para" style="top:838px">Ut enim ad minim veniam, quis nostrud exercitation ullamco laboris nisi ut aliquip ex ea commodo consequat. Duis aute irure dolor in reprehenderit in voluptate velit esse cillum dolore eu fugiat nulla pariatur.</p>
  <a class="abs read-more">READ MORE</a>
</section>

<section>
  <h2 class="abs section-title login-title">Login</h2>
  <div class="abs rule login-rule"></div>
  <div class="abs login-panel"></div>
  <span class="abs field-label" style="top:765px">USERNAME</span>
  <div class="abs field" style="top:758px"></div>
  <span class="abs field-label" style="top:807px">PASSWORD</span>
  <div class="abs field" style="top:801px"></div>
  <a class="abs btn btn-login">LOGIN</a>
  <a class="abs btn btn-new">NEW USER</a>
  <a class="abs forgot">Forgot Password</a>
</section>

<section>
  <div class="abs news"></div>
  <div class="abs news-tag">Latest<br>News</div>
  <svg class="abs news-arrow" width="30" height="50" viewBox="0 0 30 50"><path d="M0 0 L30 25 L0 50Z" fill="var(--green)"/></svg>
  <div class="abs news-head">WENN TRÄUME PLATZEN... - ANNA</div>
  <div class="abs news-date">11/5/2014</div>
  <p class="abs news-body">Diesen Blogartikel hatte ich mir anders vorgestellt... Eigentlich weiß ich schon seit Monaten Eigentlich weiß ich schon seit ...Diesen Blogartikel hatte ich mir anders vorgestellt...</p>
  <div class="abs news-pager">❮ ❯</div>
</section>

<aside>
  <div class="abs ad ad-one"><b>Your Ad Here</b><span>125x125</span></div>
  <div class="abs ad ad-two">Advertise<br>Here</div>
  <div class="abs ad ad-three"><b>Advert</b><span>125 X 125 pixels</span></div>
</aside>

<footer>
  <div class="abs footer"></div>
  <div class="abs footer-shadow"></div>
  <div class="abs foot-links">About<span class="sep">|</span>Terms<span class="sep">|</span>Privacy Policy</div>
  <div class="abs copy">All Rights Reserved. Copyrights © 2014.</div>
  <div class="abs news-label">Newsletter Signup</div>
  <div class="abs email">Email Address</div>
  <div class="abs subscribe">Subscribe</div>
  <svg class="abs phone-icon" width="40" height="40" viewBox="0 0 40 40">
    <circle cx="20" cy="20" r="18" fill="none" stroke="#777" stroke-width="2.5"/>
    <path d="M14 10 L18 10 L19 16 L16.5 18 Q19 24 23 26 L25 23.5 L31 25 L31 29 Q28 32 24 31 Q12 26 10 14 Q11 11 14 10Z" fill="#777"/>
  </svg>
  <div class="abs call-label">Call Us:</div>
  <div class="abs call-num">045-5550-0199</div>
  <div class="abs social"><i></i><i></i><i></i><i></i></div>
</footer>

</body>
</html>
```